Law Office business card design

I have a general practice specializing in criminal defense work and domestic cases. I have extensive trial and appellate experience.

Target Market(s)

general public

Industry/Entity Type

Defense

Contact Information for Business Card

Dorrington Law Office, P.A.
382 N. 4th
PO Box 5284
Salina, KS 67409-5284
(785) 555-0172
(785) 555-0198 FAX
tdorrin@quellmail.net

Requirements
Must have
• A symbol that immediately identifes the card as a legal practice.

```html
<!DOCTYPE html>
<html lang="en">
<head>
<meta charset="utf-8">
<title>Dorrington Law Office, P.A. — Business Card</title>
<link href="https://fonts.googleapis.com/css2?family=Montserrat:wght@400;500&display=swap" rel="stylesheet">
<style>
  :root {
    --backdrop: #ebebeb;
    --card: #ffffff;
    --ink-blue: #3a4aa8;
    --ink-grey: #8c8f96;
    --mark-grey: #a7a9ae;
  }
  html, body {
    margin: 0;
    padding: 0;
    width: 1200px;
    height: 900px;
    overflow: hidden;
    background: var(--backdrop);
    font-family: "Montserrat", Arial, sans-serif;
  }
  .card {
    position: absolute;
    left: 100px;
    top: 170px;
    width: 1000px;
    height: 560px;
    background: var(--card);
  }
  .brand-mark {
    position: absolute;
    left: 50%;
    top: 34px;
    width: 60px;
    height: 60px;
    margin-left: -30px;
  }
  .firm-name {
    position: absolute;
    top: 128px;
    left: 0;
    width: 100%;
    margin: 0;
    text-align: center;
    font-size: 38px;
    font-weight: 500;
    letter-spacing: 1px;
    color: var(--ink-blue);
    text-transform: uppercase;
  }
  .firm-email {
    position: absolute;
    top: 188px;
    left: 0;
    width: 100%;
    text-align: center;
    font-size: 22px;
    font-weight: 400;
    letter-spacing: 2px;
    color: var(--ink-grey);
    text-transform: uppercase;
  }
  .contact-line {
    position: absolute;
    font-size: 22px;
    font-weight: 400;
    letter-spacing: 1px;
    color: var(--ink-blue);
    text-transform: uppercase;
    white-space: nowrap;
  }
  .contact-line .label {
    color: var(--ink-grey);
    margin-right: 14px;
  }
  .fax { left: 200px; top: 298px; }
  .phone { left: 530px; top: 298px; }
  .address { left: 200px; top: 336px; }
</style>
</head>
<body>
  <section class="card">
    <svg class="brand-mark" viewBox="0 0 60 60" aria-hidden="true">
      <circle cx="30" cy="30" r="28" fill="var(--mark-grey)"/>
    </svg>
    <h1 class="firm-name">Dorrington Law Office, P.A.</h1>
    <div class="firm-email">tdorrin@quellmail.net</div>
    <div class="contact-line fax"><span class="label">F</span>(785) 555-0198</div>
    <div class="contact-line phone"><span class="label">T</span>(785) 555-0172</div>
    <div class="contact-line address"><span class="label">A</span>382 N. 4th PO Box 5284 Salina, KS 67409</div>
  </section>
</body>
</html>
```